Design a 4-page brochure for Bramble Peak Fund

Please use the content from the Updated Brochure attachment to design a 4-page 4-color glossy letter sized brochure for Bramble Peak Fund. The content and concept of the brochure are in the attached word document. Additional photos are attached, and a logo for the fund will be forthcoming (the logo is currently a contest on ArtworkHive)
We own the attached photos that can be used in brochure.

Target Market(s)

Investors

Industry/Entity Type

Investment

```html
<!DOCTYPE html>
<html lang="en">
<head>
<meta charset="utf-8">
<title>Bramble Peak Fund – Brochure Cover</title>
<link rel="stylesheet" href="https://fonts.googleapis.com/css2?family=Barlow+Semi+Condensed:wght@700&family=Oswald:wght@300&display=swap">
<style>
  :root {
    --backdrop: #e6e6e6;
    --paper: #ffffff;
    --paper-fade: #f1f1f1;
    --teal: #4a857e;
    --headline-ink: #ffffff;
    --sky-top: #3b3f9a;
    --sky-mid: #6a6fc4;
    --city-glow: #d89a4a;
    --water: #6a5aa8;
  }
  * { margin: 0; padding: 0; box-sizing: border-box; }
  html, body {
    width: 1200px;
    height: 900px;
    overflow: hidden;
    background: var(--backdrop);
  }
  .canvas {
    width: 1200px;
    height: 900px;
    display: flex;
    align-items: center;
    justify-content: center;
  }
  .cover {
    position: relative;
    width: 620px;
    height: 802px;
    background: linear-gradient(180deg, var(--paper-fade) 0%, var(--paper) 35%, var(--paper) 70%, var(--paper-fade) 100%);
    overflow: hidden;
  }
  .brand {
    position: absolute;
    left: 62px;
    top: 236px;
    display: flex;
    align-items: center;
    gap: 14px;
  }
  .brand-mark {
    width: 46px;
    height: 46px;
    border: 3px solid var(--teal);
  }
  .brand-name {
    font-family: "Barlow Semi Condensed", sans-serif;
    font-weight: 700;
    font-size: 44px;
    letter-spacing: 0.5px;
    color: var(--teal);
    text-transform: uppercase;
    line-height: 1;
  }
  .feature-band {
    position: absolute;
    left: 0;
    top: 308px;
    width: 100%;
    height: 380px;
    background: var(--teal);
  }
  .skyline-photo {
    position: absolute;
    left: 0;
    top: 22px;
    width: 100%;
    height: 208px;
    background:
      linear-gradient(180deg, transparent 55%, rgba(216,154,74,0.55) 75%, var(--water) 100%),
      linear-gradient(180deg, var(--sky-top) 0%, var(--sky-mid) 55%, var(--city-glow) 100%);
  }
  .headline {
    position: absolute;
    left: 48px;
    right: 40px;
    top: 252px;
    font-family: "Oswald", sans-serif;
    font-weight: 300;
    font-size: 30px;
    line-height: 1.08;
    color: var(--headline-ink);
    text-transform: uppercase;
    letter-spacing: 0.2px;
  }
</style>
</head>
<body>
  <main class="canvas">
    <article class="cover">
      <header class="brand">
        <span class="brand-mark"></span>
        <span class="brand-name">Bramble Peak</span>
      </header>
      <section class="feature-band">
        <div class="skyline-photo" role="img" aria-label="Photograph of a city skyline lit at dusk across the water"></div>
        <h1 class="headline">Now you can finally earn substantial monthly returns while realizing solid capital growth</h1>
      </section>
    </article>
  </main>
</body>
</html>
```